Thriving Mexican import business needs a new business card

Need a refresher of our current business card. Looking for a lighter background with the logo on one side. We will want this file to be adjustable so we can change names, emails and mobile numbers.
We are open to ideas but maintaining a professional image is critical.
Thankyou,

Target Market(s)

Anyone in food industry

Industry/Entity Type

Wholesale

Contact Information for Business Card

Mark Pendlebury
Director
Condor Provisions & Spirits Pty Ltd
5B Morrow Ct, Kelvinbrook VIC 3127
0421930576 (03) 95128460
mark@condorlatino.example.au
condorlatinoprovisionsandspirits.example.au

Font styles to use
Serif
Other font styles liked:
• NeoGram Heavy

Requirements
Must have
• Professional yet memorable
Condor logo
Nice to have
• Chilli or tequila/mexican food pictures
Should not have
• Dark background

```html
<!DOCTYPE html>
<html lang="en">
<head>
<meta charset="utf-8">
<title>Condor Provisions &amp; Spirits – Business Card</title>
<link href="https://fonts.googleapis.com/css2?family=Noto+Serif:wght@400;700&display=swap" rel="stylesheet">
<style>
  :root {
    --backdrop: #d2d2d2;
    --card-light: #ffffff;
    --card-dark: #141416;
    --ink: #141414;
    --ink-soft: #4a4a4a;
    --rule: #2a2a2a;
  }
  * { box-sizing: border-box; margin: 0; padding: 0; }
  html, body {
    width: 1125px;
    height: 1200px;
    overflow: hidden;
    background: var(--backdrop);
    font-family: "Noto Serif", serif;
  }
  .sheet {
    position: relative;
    width: 1125px;
    height: 1200px;
  }
  .card {
    position: absolute;
    left: 181px;
    width: 762px;
    height: 434px;
    border-radius: 18px;
    overflow: hidden;
  }
  .card--front { top: 141px; background: var(--card-light); color: var(--ink); }
  .card--back { top: 625px; background: var(--card-dark); color: var(--card-light); }

  /* front */
  .brand {
    position: absolute;
    right: 28px;
    top: 40px;
    display: flex;
    flex-direction: column;
    align-items: center;
    gap: 14px;
  }
  .brand__dot {
    width: 46px;
    height: 46px;
    border-radius: 50%;
    background: var(--ink);
  }
  .brand__name {
    font-weight: 700;
    font-size: 36px;
    letter-spacing: 2px;
    line-height: 1;
    text-transform: uppercase;
    color: var(--ink);
  }
  .tab {
    position: absolute;
    left: 0;
    top: 251px;
    width: 14px;
    height: 47px;
    background: var(--ink);
    border-radius: 0 10px 10px 0;
  }
  .person {
    position: absolute;
    left: 28px;
    top: 246px;
    right: 28px;
  }
  .person__name {
    font-weight: 700;
    font-size: 26px;
    line-height: 1.2;
  }
  .person__role {
    display: flex;
    align-items: center;
    gap: 10px;
    font-size: 17px;
    color: var(--ink-soft);
    margin-top: 2px;
  }
  .person__role::after {
    content: "";
    flex: 1;
    height: 1px;
    background: var(--rule);
    margin-top: 4px;
  }
  .contacts {
    position: absolute;
    left: 28px;
    top: 320px;
    list-style: none;
    font-size: 16px;
    line-height: 23px;
    color: var(--ink-soft);
  }
  .contacts li { display: flex; align-items: center; gap: 6px; }
  .contacts svg { width: 12px; height: 12px; fill: var(--ink); flex: none; }
  .company {
    position: absolute;
    right: 28px;
    top: 366px;
    text-align: right;
    font-size: 16px;
    line-height: 23px;
    color: var(--ink-soft);
  }

  /* back */
  .brand--back {
    position: absolute;
    left: 0;
    right: 0;
    top: 112px;
    display: flex;
    flex-direction: column;
    align-items: center;
    gap: 28px;
  }
  .brand--back .brand__dot { width: 80px; height: 80px; background: var(--card-light); }
  .brand--back .brand__name { font-size: 62px; color: var(--card-light); letter-spacing: 3px; }
</style>
</head>
<body>
<main class="sheet">
  <section class="card card--front" aria-label="Business card front">
    <div class="brand">
      <span class="brand__dot"></span>
      <span class="brand__name">Condor</span>
    </div>

    <span class="tab"></span>
    <div class="person">
      <h1 class="person__name">Mark Pendlebury</h1>
      <p class="person__role">Director</p>
    </div>

    <ul class="contacts">
      <li>
        <svg viewBox="0 0 24 24" aria-hidden="true"><path d="M6.6 10.8a15.1 15.1 0 0 0 6.6 6.6l2.2-2.2a1 1 0 0 1 1-.25 11.4 11.4 0 0 0 3.6.57 1 1 0 0 1 1 1V20a1 1 0 0 1-1 1A17 17 0 0 1 3 4a1 1 0 0 1 1-1h3.5a1 1 0 0 1 1 1c0 1.25.2 2.45.57 3.57a1 1 0 0 1-.25 1z"/></svg>
        0421930576
      </li>
      <li>
        <svg viewBox="0 0 24 24" aria-hidden="true"><path d="M7 1h10a2 2 0 0 1 2 2v18a2 2 0 0 1-2 2H7a2 2 0 0 1-2-2V3a2 2 0 0 1 2-2zm0 3v14h10V4zm5 15.5a1.2 1.2 0 1 0 0 2.4 1.2 1.2 0 0 0 0-2.4z"/></svg>
        (03) 95128460
      </li>
      <li>
        <svg viewBox="0 0 24 24" aria-hidden="true"><path d="M2 5h20v14H2zm2 2v.4l8 5.2 8-5.2V7zm0 2.8V17h16V9.8l-8 5.2z"/></svg>
        mark@condorlatino.example.au
      </li>
      <li>
        <svg viewBox="0 0 24 24" aria-hidden="true"><path d="M12 2a10 10 0 1 0 0 20 10 10 0 0 0 0-20zm-1 17.9A8 8 0 0 1 4.2 10.2L9 15v1a2 2 0 0 0 2 2zm6.9-2.5A2 2 0 0 0 16 16h-1v-3a1 1 0 0 0-1-1H8v-2h2a1 1 0 0 0 1-1V7h2a2 2 0 0 0 2-2v-.4a8 8 0 0 1 2.9 12.8z"/></svg>
        condorlatinoprovisionsandspirits.example.au
      </li>
    </ul>

    <address class="company" style="font-style: normal;">
      Condor Provisions &amp; Spirits Pty Ltd<br>
      5B Morrow Ct, Kelvinbrook VIC 3127
    </address>
  </section>

  <section class="card card--back" aria-label="Business card back">
    <div class="brand brand--back">
      <span class="brand__dot"></span>
      <span class="brand__name">Condor</span>
    </div>
  </section>
</main>
</body>
</html>
```